Business cards to launch an education platform

Hi,
I am looking at having new business cards designed.
I am a startup, developing a web platform for schools and university, the education world. It's an online assessment system.
I would like a card that looks classy, and that is using the colors and the font of my logo.

I have attached:
1) my logo
2) A business card that I have designed quickly so you can have all the information required in the card, but I really don't like it.
3) The font that I am using (Lato Regular) to design my web platform
4) Some screenshots of my web platform so you can have a look at the style that I have.

Target Market(s)

Major market: Education system: Schools and university
Minor markets: Business in general

Industry/Entity Type

Business

Contact Information for Business Card

Tessa Vinall
Director

M: 0487 312 950
E: tessa.vinall@copperLoomVentures.com.au

Requirements
Must have
• The colors of my logo

```html
<!DOCTYPE html>
<html lang="en">
<head>
<meta charset="utf-8">
<title>Copper Loom Ventures — Business Cards</title>
<link rel="stylesheet" href="https://fonts.googleapis.com/css2?family=Lato:wght@400;700&display=swap">
<style>
  :root {
    --navy: #0f4a80;
    --navy-deep: #0b3d6e;
    --sky: #2eaee3;
    --ink: #4a4f55;
    --paper: #ffffff;
    --backdrop: #e9ebee;
  }
  * { margin: 0; padding: 0; box-sizing: border-box; }
  html, body { width: 1200px; height: 950px; overflow: hidden; }
  body {
    background: var(--backdrop);
    font-family: "Lato", sans-serif;
    position: relative;
  }
  .card {
    position: absolute;
    left: 220px;
    width: 760px;
    height: 434px;
    overflow: hidden;
    box-shadow: 0 6px 18px rgba(0,0,0,0.18);
  }
  /* Front */
  .card-front {
    top: 28px;
    background: var(--navy);
    color: var(--paper);
  }
  .front-brand {
    position: absolute;
    left: 0; right: 0; top: 160px;
    display: flex;
    align-items: center;
    justify-content: center;
    gap: 22px;
  }
  .brand-mark {
    width: 70px; height: 70px;
    background: var(--paper);
  }
  .brand-name {
    font-weight: 400;
    font-size: 40px;
    letter-spacing: 2px;
  }
  .front-web {
    position: absolute;
    left: 0; right: 0; top: 330px;
    text-align: center;
    font-size: 17px;
    letter-spacing: 0.5px;
  }
  /* Back */
  .card-back {
    top: 488px;
    background: var(--paper);
  }
  .back-brand {
    position: absolute;
    right: 50px; top: 46px;
    display: flex;
    align-items: center;
    gap: 16px;
  }
  .back-brand .brand-mark { width: 58px; height: 58px; background: var(--navy); }
  .back-brand .brand-name { color: var(--navy); font-size: 32px; letter-spacing: 1.5px; }
  .rule {
    position: absolute;
    left: 330px; right: 50px; top: 142px;
    height: 1px;
    background: var(--navy);
  }
  .person {
    position: absolute;
    left: 46px; top: 232px;
  }
  .person-name { color: var(--navy); font-weight: 700; font-size: 27px; }
  .person-role { color: var(--sky); font-size: 18px; margin-top: 2px; }
  .contacts {
    position: absolute;
    left: 46px; top: 322px;
    list-style: none;
    color: var(--ink);
    font-size: 17px;
  }
  .contacts li { display: flex; align-items: center; gap: 12px; margin-bottom: 8px; }
  .contacts svg { width: 18px; height: 18px; flex: none; }
  .base-bands { position: absolute; left: 0; bottom: 0; width: 760px; height: 40px; }
</style>
</head>
<body>
  <section class="card card-front" aria-label="Card front">
    <div class="front-brand">
      <span class="brand-mark"></span>
      <span class="brand-name">Copper Loom Ventures</span>
    </div>
    <p class="front-web">www.copperLoomVentures.com.au</p>
  </section>

  <section class="card card-back" aria-label="Card back">
    <div class="back-brand">
      <span class="brand-mark"></span>
      <span class="brand-name">Copper Loom Ventures</span>
    </div>
    <div class="rule"></div>
    <div class="person">
      <h1 class="person-name">Tessa Vinall</h1>
      <p class="person-role">Director</p>
    </div>
    <ul class="contacts">
      <li>
        <svg viewBox="0 0 18 18" aria-hidden="true"><rect x="4" y="1" width="10" height="16" rx="2" fill="none" stroke="var(--navy)" stroke-width="1.8"/><circle cx="9" cy="14" r="1" fill="var(--navy)"/></svg>
        <span>0487 312 950</span>
      </li>
      <li>
        <svg viewBox="0 0 18 18" aria-hidden="true"><rect x="1" y="4" width="16" height="11" fill="var(--navy)"/><path d="M1 4 L9 10 L17 4" fill="none" stroke="#fff" stroke-width="1.4"/></svg>
        <span>tessa.vinall@copperLoomVentures.com.au</span>
      </li>
    </ul>
    <svg class="base-bands" viewBox="0 0 760 40" aria-hidden="true">
      <rect x="0" y="24" width="760" height="16" fill="var(--navy-deep)"/>
      <polygon points="540,14 760,14 760,24 540,24" fill="var(--sky)"/>
    </svg>
  </section>
</body>
</html>
```